Company Values One-Pager

We're a recruitment firm based in Singapore, focused on the startup tech and VC sectors. www.brelvanhire.com

As we're now at the point of growing and hiring, we want a one-pager (PDF or whatever) that summarises us and our company values.

I've attached a short PowerPoint that goes into the values etc.

Font styles to use
Sans Serif

Requirements
Must have
• We like a 'clean' look. Our logo is bright and simple, and that's what we're looking for.
• The official colour code for the logo is seafoam green
• www.huepondlab.com/color/71EEB8/sea_foam_green
• Our website also gives a good insight.
• I'd like logos that summarise each value alongside them. i.e + for positivity, a letter for delivery etc. (Just ideas - please innovate!)
Should not have
• Nothing dark - just keep it simple and fresh

```html
<!DOCTYPE html>
<html lang="en">
<head>
<meta charset="utf-8">
<title>Brelvan Hire – Our Values</title>
<link rel="stylesheet" href="https://fonts.googleapis.com/css2?family=Roboto:ital,wght@0,100;0,300;0,400;0,500;0,700;0,900;1,400&display=swap">
<style>
  :root {
    --seafoam: #7cc89a;
    --seafoam-dark: #5aa67c;
    --blue: #0a73bd;
    --grey-band: #d4d5d7;
    --grey-divider: #e6e7e8;
    --grey-shape: #8e8f92;
    --text: #3a3a3a;
    --text-soft: #555759;
    --rule: #9a9a9a;
    --paper: #ffffff;
    --paper-soft: #f2f5f4;
  }
  * { box-sizing: border-box; margin: 0; padding: 0; }
  html, body { width: 848px; height: 1200px; overflow: hidden; background: var(--paper); }
  body { font-family: "Roboto", Arial, sans-serif; color: var(--text); }
  .sheet { position: relative; width: 848px; height: 1200px; overflow: hidden; background: var(--paper); }

  .lower-ground { position: absolute; left: 0; top: 822px; width: 848px; height: 378px; background: var(--paper-soft); }
  .frame { position: absolute; left: 22px; top: 22px; width: 786px; height: 1150px; border: 2px solid var(--seafoam); }
  .corner { position: absolute; }
  .corner-top { left: 0; top: 0; }
  .corner-bottom { left: 0; bottom: 0; }

  .brand-name { position: absolute; left: 616px; top: 100px; font-weight: 500; font-size: 22px; line-height: 1; color: var(--seafoam); white-space: nowrap; }

  .title { position: absolute; left: 70px; top: 160px; line-height: 1; }
  .title .light { display: block; font-weight: 100; font-size: 104px; letter-spacing: 1px; color: var(--text); }
  .title .heavy { display: block; margin-top: -24px; font-weight: 900; font-size: 128px; letter-spacing: -1px; color: var(--blue); }

  .name-band { position: absolute; left: 0; top: 393px; width: 366px; height: 40px; }
  .name-band span { position: absolute; left: 72px; top: 9px; font-weight: 700; font-size: 20px; color: var(--paper); white-space: nowrap; }

  .facts { position: absolute; top: 460px; font-size: 13px; line-height: 17px; color: var(--text); }
  .facts-left { left: 71px; width: 330px; }
  .facts-right { left: 424px; width: 370px; }
  .fact { display: flex; margin-bottom: 11px; }
  .fact .label { font-weight: 700; color: var(--blue); white-space: nowrap; margin-right: 4px; }

  .section-rule { position: absolute; top: 606px; height: 2px; }
  .section-rule.left { left: 150px; width: 118px; background: linear-gradient(90deg, transparent, var(--blue)); }
  .section-rule.right { left: 552px; width: 118px; background: linear-gradient(90deg, var(--blue), transparent); }
  .section-tag { position: absolute; left: 275px; top: 586px; width: 274px; height: 40px; }
  .section-tag span { position: absolute; left: 0; width: 274px; top: 9px; text-align: center; font-weight: 700; font-size: 20px; color: var(--paper); }

  .values-band { position: absolute; left: 0; top: 626px; width: 848px; height: 196px; background: var(--grey-band); display: flex; padding: 0 70px 0 72px; }
  .value { position: relative; flex: 1; text-align: center; padding-top: 22px; }
  .value + .value::before { content: ""; position: absolute; left: 0; top: 30px; bottom: 20px; width: 1px; background: var(--grey-divider); }
  .value .icon { width: 52px; height: 52px; margin: 0 auto; border-radius: 50%; background: var(--paper); box-shadow: 0 1px 3px rgba(0,0,0,0.25); display: flex; align-items: center; justify-content: center; }
  .value h3 { margin-top: 10px; font-weight: 400; font-size: 17px; color: var(--blue); }
  .value p { margin-top: 13px; font-size: 14px; line-height: 17px; color: var(--text-soft); }

  .quote-open, .quote-close { position: absolute; font-size: 54px; font-weight: 900; color: #444; line-height: 1; }
  .quote-open { left: 68px; top: 838px; }
  .quote-close { left: 722px; top: 1082px; }
  .quote-rule { position: absolute; height: 1px; background: var(--rule); }
  .quote-rule.top { left: 106px; top: 858px; width: 650px; }
  .quote-rule.bottom { left: 72px; top: 1098px; width: 646px; }

  .quote { position: absolute; display: flex; gap: 13px; font-size: 10.5px; line-height: 13.5px; font-style: italic; color: var(--text); }
  .quote .portrait { flex: none; width: 64px; height: 78px; border: 2px solid #bfc1c2; }
  .quote blockquote { padding-top: 6px; }
  .quote cite { display: block; margin-top: 5px; font-style: italic; }
  .q1 { left: 71px; top: 887px; width: 210px; }
  .q2 { left: 291px; top: 887px; width: 470px; }
  .q2 blockquote { padding-top: 18px; }
  .q3 { left: 71px; top: 992px; width: 210px; }
  .q4 { left: 291px; top: 992px; width: 200px; }
  .q5 { left: 507px; top: 992px; width: 250px; }
  .q5 blockquote { padding-top: 0; }
</style>
</head>
<body>
<div class="sheet">
  <div class="lower-ground"></div>
  <div class="frame"></div>

  <svg class="corner corner-top" width="600" height="160" viewBox="0 0 600 160" aria-hidden="true">
    <polygon points="0,0 480,0 568,156 0,22" fill="var(--seafoam)"/>
    <polygon points="0,20 500,12 568,156" fill="var(--seafoam-dark)" opacity="0.55"/>
    <polygon points="0,24 280,60 0,148" fill="var(--grey-shape)"/>
  </svg>

  <svg class="corner corner-bottom" width="360" height="90" viewBox="0 0 360 90" aria-hidden="true">
    <polygon points="0,90 0,30 180,72 230,90" fill="var(--seafoam)"/>
    <polygon points="0,90 340,32 220,90" fill="var(--grey-shape)"/>
  </svg>

  <div class="brand-name">BRELVAN HIRE</div>

  <h1 class="title">
    <span class="light">OUR</span>
    <span class="heavy">VALUES</span>
  </h1>

  <div class="name-band">
    <svg width="366" height="40" viewBox="0 0 366 40" aria-hidden="true">
      <polygon points="0,0 340,0 366,40 0,40" fill="var(--seafoam)"/>
    </svg>
    <span>BRELVAN HIRE</span>
  </div>

  <div class="facts facts-left">
    <div class="fact"><span class="label">WHAT</span><span>- We are the ‘recruitment partner for the startup ecosystem in South-East Asia’; partnering with Venture Capital and startup tech firms, HQ’d out of Singapore.</span></div>
    <div class="fact"><span class="label">WHO</span><span>- Established by Dara Tenh &amp; Owen Farrow</span></div>
  </div>
  <div class="facts facts-right">
    <div class="fact"><span class="label">WHEN</span><span>- Opened our doors in September 2016</span></div>
    <div class="fact"><span class="label">LONGER-TERM GOAL</span><span>- Asia and Global expansion</span></div>
    <div class="fact"><span class="label">CORE VALUES</span><span>- Positivity &nbsp;– &nbsp;Proactivity<br>&nbsp;&nbsp;Teamwork &nbsp;– &nbsp;Delivery</span></div>
  </div>

  <div class="section-rule left"></div>
  <div class="section-rule right"></div>
  <div class="section-tag">
    <svg width="274" height="40" viewBox="0 0 274 40" aria-hidden="true">
      <polygon points="8,0 274,0 264,40 0,40" fill="var(--blue)"/>
    </svg>
    <span>OUR CORE VALUES</span>
  </div>

  <section class="values-band">
    <div class="value">
      <div class="icon">
        <svg width="30" height="30" viewBox="0 0 30 30" aria-hidden="true">
          <rect x="3" y="13" width="6" height="13" rx="1" fill="#444"/>
          <path d="M11 13 L16 4 Q19 3 19 7 L18 11 H25 Q28 12 27 15 L24 25 Q23 27 21 27 H11 Z" fill="none" stroke="#444" stroke-width="2.2" stroke-linejoin="round"/>
        </svg>
      </div>
      <h3>POSITIVITY</h3>
      <p>We look on the<br>bright side…<br>and don’t let limiting<br>beliefs hold us back</p>
    </div>
    <div class="value">
      <div class="icon">
        <svg width="32" height="32" viewBox="0 0 32 32" aria-hidden="true">
          <circle cx="16" cy="14" r="6.5" fill="none" stroke="#444" stroke-width="1.6"/>
          <rect x="13" y="21" width="6" height="4" fill="none" stroke="#444" stroke-width="1.4"/>
          <line x1="14" y1="27" x2="18" y2="27" stroke="#444" stroke-width="1.4"/>
          <g stroke="#444" stroke-width="1.4">
            <line x1="16" y1="2" x2="16" y2="5"/><line x1="5" y1="14" x2="8" y2="14"/><line x1="24" y1="14" x2="27" y2="14"/>
            <line x1="8" y1="6" x2="10" y2="8"/><line x1="24" y1="6" x2="22" y2="8"/>
          </g>
        </svg>
      </div>
      <h3>PROACTIVITY</h3>
      <p>We don’t wait…<br>we make things<br>happen</p>
    </div>
    <div class="value">
      <div class="icon">
        <svg width="32" height="30" viewBox="0 0 32 30" aria-hidden="true">
          <circle cx="16" cy="9" r="5" fill="#444"/>
          <path d="M7 24 Q7 15 16 15 Q25 15 25 24 Z" fill="#444"/>
          <circle cx="7" cy="11" r="3.5" fill="#444"/>
          <path d="M1 23 Q1 16 7 16 Q9 16 9 17 Q6 19 6 23 Z" fill="#444"/>
          <circle cx="25" cy="11" r="3.5" fill="#444"/>
          <path d="M31 23 Q31 16 25 16 Q23 16 23 17 Q26 19 26 23 Z" fill="#444"/>
        </svg>
      </div>
      <h3>TEAMWORK</h3>
      <p>We work together…<br>to solve problems,<br>find solutions, and<br>celebrate the good times</p>
    </div>
    <div class="value">
      <div class="icon">
        <svg width="32" height="32" viewBox="0 0 32 32" aria-hidden="true">
          <circle cx="18" cy="17" r="9" fill="none" stroke="#444" stroke-width="2"/>
          <rect x="16" y="4" width="4" height="3" fill="#444"/>
          <line x1="18" y1="17" x2="22" y2="13" stroke="#444" stroke-width="2"/>
          <g stroke="#444" stroke-width="1.8"><line x1="2" y1="13" x2="7" y2="13"/><line x1="1" y1="17" x2="7" y2="17"/><line x1="2" y1="21" x2="7" y2="21"/></g>
        </svg>
      </div>
      <h3>DELIVERY</h3>
      <p>We do what we say we’re<br>going to do… for our<br>candidates, clients, and<br>colleagues alike</p>
    </div>
  </section>

  <div class="quote-open">“</div>
  <div class="quote-rule top"></div>

  <figure class="quote q1">
    <div class="portrait" role="img" aria-label="Portrait photo of Lin Haoran" style="background: linear-gradient(135deg,#5a5a5a,#1f1f1f);"></div>
    <blockquote>“Today is hard, tomorrow will be worse, but the day after tomorrow will be sunshine”<cite>Lin Haoran, Quorra Trade</cite></blockquote>
  </figure>
  <figure class="quote q2">
    <div class="portrait" role="img" aria-label="Portrait photo of Cal Brenner in a spacesuit" style="background: linear-gradient(135deg,#c9c3bd,#8a6a55);"></div>
    <blockquote>“There are people who make things happen, there are people who watch things happen and there are people who wonder what happened.<br>To be successful, you need to be a person who makes things happen”<cite>Cal Brenner, Astronaut</cite></blockquote>
  </figure>
  <figure class="quote q3">
    <div class="portrait" role="img" aria-label="Black and white portrait photo of Elias Rowe" style="background: linear-gradient(135deg,#9a9a9a,#1a1a1a);"></div>
    <blockquote>“Great things in business are never done by one person, they’re done by a team of people”<cite>Elias Rowe, Pellhaven</cite></blockquote>
  </figure>
  <figure class="quote q4">
    <div class="portrait" role="img" aria-label="Photo of Mira Santos speaking at an event" style="background: linear-gradient(135deg,#8fb0c4,#3d4a3f);"></div>
    <blockquote>“Instead of just offering advice, we actually deliver solutions”<cite>Mira Santos, Founder Of Tessel</cite></blockquote>
  </figure>
  <figure class="quote q5">
    <div class="portrait" role="img" aria-label="Portrait photo of Henrik Aldane" style="background: linear-gradient(135deg,#6d7a8a,#2e3440);"></div>
    <blockquote>There’s nothing more invigorating than being deeply involved with a small company and a young team of founders out to do something incredibly special.<cite>Henrik Aldane, Venture Capitalist</cite></blockquote>
  </figure>

  <div class="quote-rule bottom"></div>
  <div class="quote-close">”</div>
</div>
</body>
</html>
```